Post Lockdown Ortho Special

We are running a special for (Ortho) Braces/Clear Aligner (Quorventa), till July 31st 2020. Up to $2,000 off with free Consultation and Xrays.

We need a ad to run in different formats.

Maybe something with: what better time to get braces when you have to wear a mask all the time.

Trying to rebuild our business and get people in for free consultations.

```html
<!DOCTYPE html>
<html lang="en">
<head>
<meta charset="utf-8">
<title>Post Lockdown Ortho Special</title>
<link rel="stylesheet" href="https://fonts.googleapis.com/css2?family=Anton&family=Oswald:wght@600&family=Open+Sans:wght@700&display=swap">
<style>
  :root {
    --purple: #6b4a9b;
    --sun: #f8bb2b;
    --sun-light: #fcc63f;
    --headline: #ffd966;
    --white: #ffffff;
    --grey-light: #d6d6d6;
    --grey-dark: #8e8e8e;
    --icon-tint: #cfe9f6;
  }
  * { margin: 0; padding: 0; box-sizing: border-box; }
  html, body { width: 843px; height: 1200px; overflow: hidden; background: var(--purple); }
  .ad { position: relative; width: 843px; height: 1200px; background: var(--purple); overflow: hidden; }
  .photo {
    position: absolute; left: 0; top: 300px; width: 843px; height: 645px;
    background: radial-gradient(ellipse at 72% 60%, #e9a52a 0%, var(--sun-light) 45%, var(--sun) 100%);
  }
  .shapes { position: absolute; inset: 0; }
  .braces-art {
    position: absolute; left: 585px; top: 898px; width: 185px; height: 86px;
    border-radius: 14px;
    background: linear-gradient(180deg, var(--icon-tint) 0%, #e4f3fa 100%);
  }
  .headline {
    position: absolute; left: 0; right: 0; top: 24px; text-align: center;
    font-family: "Oswald", sans-serif; font-weight: 600; color: var(--headline);
    line-height: 1; white-space: nowrap;
  }
  .headline .big { font-size: 92px; letter-spacing: -1px; }
  .headline .mid { font-size: 58px; }
  .headline .line2 { display: block; font-size: 61px; margin-top: 18px; }
  .practice {
    position: absolute; left: 100px; top: 276px; display: flex; align-items: center; gap: 12px;
    font-family: "Open Sans", sans-serif; font-weight: 700; color: var(--purple);
  }
  .practice .dot { width: 58px; height: 58px; border-radius: 50%; background: var(--purple); flex: none; }
  .practice .name { font-size: 17px; line-height: 1.15; text-transform: uppercase; letter-spacing: 0.5px; }
  .practice .doctor { font-size: 9px; letter-spacing: 1px; display: block; margin-top: 3px; }
  .tagline {
    position: absolute; left: 20px; width: 380px; top: 412px; text-align: center;
    font-family: "Anton", sans-serif; font-weight: 400; color: var(--purple); text-transform: uppercase;
    line-height: 1.16;
  }
  .tagline span { display: block; font-size: 68px; transform: scaleX(1.12); }
  .tagline .now { font-size: 118px; line-height: 1.02; margin-top: -8px; }
  .offer {
    position: absolute; left: 0; right: 0; top: 1028px; text-align: center;
    font-family: "Open Sans", sans-serif; font-weight: 700; color: var(--headline);
    font-size: 34px; line-height: 1.3;
  }
  .offer .till { font-size: 30px; font-family: "Oswald", sans-serif; }
  .offer .date { font-family: "Oswald", sans-serif; font-size: 64px; line-height: 1.1; }
</style>
</head>
<body>
<div class="ad">
  <div class="photo" role="img" aria-label="Photo of a smiling family in matching mustard shirts wearing face masks and making OK hand signs, on a yellow backdrop"></div>

  <svg class="shapes" width="843" height="1200" viewBox="0 0 843 1200" aria-hidden="true">
    <polygon points="0,0 843,0 843,305 640,305 580,232 522,232 376,354 0,354 0,262" fill="var(--purple)"/>
    <polygon points="0,262 560,262 440,354 0,354" fill="var(--white)"/>
    <polygon points="376,354 522,230 580,230 500,305" fill="var(--grey-light)"/>
    <polygon points="500,305 580,230 640,305" fill="var(--grey-dark)"/>
    <polygon points="380,987 470,893 843,893 843,987" fill="var(--white)"/>
    <polygon points="0,987 843,987 843,1200 0,1200" fill="var(--purple)"/>
    <polygon points="209,943 345,943 277,1019" fill="var(--grey-dark)"/>
    <polygon points="345,943 434,943 325,1024 272,1024" fill="var(--grey-light)"/>
  </svg>

  <div class="braces-art" role="img" aria-label="Illustration of a row of teeth with braces"></div>

  <h1 class="headline">
    <span class="big">Up to $2,000</span> <span class="mid">off with</span>
    <span class="line2">free Consultation and Xrays</span>
  </h1>

  <div class="practice">
    <span class="dot"></span>
    <span class="name">Ridgeview<br>Family Dentistry<span class="doctor">Dr Maren Holt</span></span>
  </div>

  <h2 class="tagline">
    <span>It is the</span>
    <span>better time</span>
    <span>to get</span>
    <span>braces</span>
    <span class="now">Now!</span>
  </h2>

  <p class="offer">
    We are running a special for (Ortho)<br>
    Braces/Clear Aligner (Quorventa),<br>
    <span class="till">till</span> <span class="date">July 31st 2020</span>
  </p>
</div>
</body>
</html>
```